WordPress Website for Pain Relief Clinic

I need a WordPress website designed for my laser pain relief clinic. It needs to be a professional, responsive design with 7 pages: Home, Why Choose Us, Treatable Conditions, Testimonials, FAQ, Franchising, Contact Us. Here is logo: https://files.brivoltcdn.com/media.t-w-e-n.com/sitebuilder/472/CalvexaLogoHighQuality.png

Target Market(s)

people with pain,elderly adults,injuries,soreness

Industry/Entity Type

Clinic

Number of Pages Required

5+ page

Colors
0792cd
85abd2

```html
<!DOCTYPE html>
<html lang="en">
<head>
<meta charset="utf-8">
<title>Calvexa Pain Treatment Center</title>
<link href="https://fonts.googleapis.com/css2?family=Mulish:ital,wght@0,400;0,600;0,700;0,800;1,400&display=swap" rel="stylesheet">
<style>
:root{
  --ink:#333333;
  --brand:#1e5fa8;
  --brand-dark:#123f73;
  --panel:#1a56a0;
  --title:#1f5d9c;
  --topbar:#1f1f1f;
  --footer:#2a2a2a;
  --white:#ffffff;
  --muted:#555555;
}
*{margin:0;padding:0;box-sizing:border-box}
html,body{width:981px;height:1200px;overflow:hidden;background:var(--white)}
body{position:relative;font-family:"Mulish",Arial,sans-serif;color:var(--ink)}
.abs{position:absolute}

.topbar{left:0;top:0;width:981px;height:39px;background:var(--topbar)}
.social{left:124px;top:9px;display:flex;gap:11px}
.social span{width:21px;height:21px;border-radius:50%;background:#5b86b8;display:block}
.social span:nth-child(3){background:#d9534f}
.social span:nth-child(2),.social span:nth-child(4){background:#4fa8d6}
.top-phone{right:109px;top:12px;color:#e8e8e8;font-size:11.5px;display:flex;align-items:center;gap:6px}

.header{left:0;top:39px;width:981px;height:95px;background:var(--white)}
.logo{left:62px;top:63px;font-size:40px;font-weight:800;color:var(--brand);letter-spacing:-1px;line-height:1}
.nav{left:284px;top:85px;display:flex;font-size:13px;color:var(--ink)}
.nav a{color:inherit;text-decoration:none;margin-right:21px}

.hero{left:0;top:134px;width:981px;height:407px;background:linear-gradient(90deg,#3e4d55 0%,#5a6b74 45%,#43535b 100%)}

.contact-panel{left:641px;top:134px;width:255px;height:390px;background:var(--panel)}
.panel-head{left:0;top:0;width:255px;height:42px;background:#15498a;color:var(--white);font-size:15.5px;padding:12px 0 0 29px}
.panel-head svg{position:absolute;right:16px;top:16px}
.panel-intro{left:18px;top:66px;width:222px;text-align:center;color:var(--white);font-size:9.3px;line-height:1.35}
.field{left:20px;width:214px;background:var(--white);color:#9a9a9a;font-size:9.5px;padding:0 16px}
.f1{top:110px;height:34px;line-height:34px}
.f2{top:158px;height:34px;line-height:34px}
.f3{top:207px;height:60px;padding-top:11px}
.send{left:80px;top:286px;width:97px;height:33px;background:var(--brand-dark);color:var(--white);font-size:12px;font-weight:700;text-align:center;line-height:33px}
.call{left:28px;top:340px;color:var(--white);font-size:15px;display:flex;align-items:baseline;gap:14px}
.call strong{font-size:21px;font-weight:800;letter-spacing:-.5px}

.welcome{left:0;top:578px;width:981px;text-align:center;color:var(--title);font-size:29px;font-weight:400}
.intro{left:128px;top:639px;width:725px;text-align:center;color:var(--muted);font-size:10.2px;line-height:1.36}

.card{top:759px;width:240px;height:167px;overflow:hidden;border:1px solid #c9d4e2}
.card-photo{left:0;top:0;width:100%;height:128px}
.card-label{left:0;top:128px;width:100%;height:39px;background:#2f67a8;color:var(--white);font-size:17px;font-weight:800;text-align:center;line-height:39px}
.c1{left:103px}
.c1 .card-photo{background:linear-gradient(135deg,#9fe0ee,#e9d3c6 55%,#c9c9cc)}
.c2{left:377px;background:linear-gradient(180deg,#2a64a8,#2d5f98)}
.c3{left:647px}
.c3 .card-photo{background:linear-gradient(135deg,#b7b2ad,#d9d5d0 50%,#8c8782)}
.faq-title{left:0;top:17px;width:100%;text-align:center;color:var(--white);font-size:17px;font-weight:800}
.faq-text{left:20px;top:46px;width:198px;text-align:center;color:var(--white);font-size:10px;line-height:1.38}
.read{left:72px;top:123px;width:92px;height:26px;border:1px solid var(--white);color:var(--white);font-size:11px;font-weight:700;text-align:center;line-height:24px}

.testimonial{left:0;top:968px;width:981px;height:178px;background:linear-gradient(90deg,#3e3430,#5a4a42 50%,#3e3430)}
.avatar{left:174px;top:1016px;width:79px;height:79px;border-radius:50%;background:radial-gradient(circle at 50% 40%,#e3c3a6,#c99a74 60%,#e8e4df);border:2px solid #d8d2cc}
.quote-mark{left:293px;top:1003px;color:#d8d8d8;font-size:26px;font-style:italic;font-family:Georgia,serif}
.quote{left:316px;top:1015px;width:493px;color:#e6e6e6;font-size:13.6px;font-style:italic;text-align:center;line-height:1.35}
.author{left:0;top:1076px;width:1096px;text-align:center;color:#e6e6e6;font-size:15px}

.footer{left:0;top:1146px;width:981px;height:54px;background:var(--footer);color:#f0f0f0;font-size:9.8px}
.footer .left{left:129px;top:20px}
.footer .right{right:109px;top:21px}
</style>
</head>
<body>

<div class="abs topbar"></div>
<div class="abs social" aria-label="Social links"><span></span><span></span><span></span><span></span></div>
<div class="abs top-phone">
  <svg width="12" height="12" viewBox="0 0 24 24" fill="#e8e8e8"><path d="M6.6 10.8a15.1 15.1 0 0 0 6.6 6.6l2.2-2.2c.3-.3.7-.4 1-.2 1.1.4 2.3.6 3.6.6.6 0 1 .4 1 1V20c0 .6-.4 1-1 1C10.6 21 3 13.4 3 4c0-.6.4-1 1-1h3.5c.6 0 1 .4 1 1 0 1.3.2 2.5.6 3.6.1.3 0 .7-.2 1z"/></svg>
  (555) 014-2290
</div>

<div class="abs header"></div>
<div class="abs logo">Calvexa</div>
<nav class="abs nav">
  <a href="#">Home</a><a href="#">Why Choose Us</a><a href="#">Treatable</a><a href="#" style="margin-right:24px">Conditions Testimonials</a><a href="#" style="margin-right:32px">FAQ</a><a href="#">Franchising</a><a href="#">Contact Us</a>
</nav>

<div class="abs hero" role="img" aria-label="Photo of a patient's back shown in x-ray style with the spine highlighted, against a grey wall"></div>

<div class="abs contact-panel">
  <div class="abs panel-head">Contact Us
    <svg width="28" height="10" viewBox="0 0 28 10"><path d="M1 1 L14 8 L27 1" stroke="#fff" stroke-width="2.5" fill="none"/></svg>
  </div>
  <p class="abs panel-intro">Take the first step toward finding pain relief, is by filling the form below</p>
  <div class="abs field f1">First/ Last &nbsp;Name</div>
  <div class="abs field f2">Email Address</div>
  <div class="abs field f3">Message</div>
  <div class="abs send">Send</div>
  <div class="abs call">Call Us <strong>(555) 014-2290</strong></div>
</div>

<h1 class="abs welcome">Welcome to Calvexa Pain Treatment Center</h1>
<p class="abs intro">Lorem ipsum dolor sit amet, consectetur adipiscing elit. Curabitur cursus turpis a congue ultricies. Praesent commodo ipsum quis pellentesque euismod. Fusce rhoncus sapien mi, non venenatis neque tristique eget. Morbi eget lacinia metus. Interdum et malesuada fames ac ante ipsum primis in faucibus. Vestibulum leo sem, tincidunt ac ornare vel, scelerisque quis sapien. Aliquam erat libero, accumsan malesuada odio sit amet, bibendum pellentesque nulla. Curabitur a laoreet enim. Cras at sollicitudin libero, sed egestas mi. Duis accumsan enim at rutrum vestibulum. Suspendisse egestas mauris sapien, at tincidunt felis aliquet sed.</p>

<div class="abs card c1">
  <div class="abs card-photo" role="img" aria-label="Photo of a laser pen treatment applied to a bare foot"></div>
  <div class="abs card-label">TREATABLE</div>
</div>
<div class="abs card c2">
  <div class="abs faq-title">FAQ</div>
  <p class="abs faq-text">Lorem ipsum dolor sit amet, consectetur adipiscing elit. Curabitur cursus turpis a congue ultricies.pellentesque euismod. Fusce rhoncus sapien mi, non venenatis neque tristique eget.</p>
  <div class="abs read">Read More</div>
</div>
<div class="abs card c3">
  <div class="abs card-photo" role="img" aria-label="Photo of a hand holding a smartphone showing a notification"></div>
  <div class="abs card-label">CONTACT US</div>
</div>

<section class="abs testimonial" role="img" aria-label="Blurred background photo of a treatment device in use"></section>
<div class="abs avatar" role="img" aria-label="Portrait photo of the client giving the testimonial"></div>
<div class="abs quote-mark">&ldquo;</div>
<p class="abs quote">Lorem ipsum dolor sit amet, consectetur adipiscing elit. Curabitur cursus turpis a congue ultricies. Praesent commodo ipsum quis pellentesque euismod. Fusce rhoncus sapien mi, non venenatis nequere</p>
<p class="abs author">- Anonymous</p>

<footer class="abs footer">
  <div class="abs left">48 Harbor Lane &bull; (555) 014-2290</div>
  <div class="abs right">&copy;2015 Calvexa Pain Treatment Center. All rights reserved.</div>
</footer>

</body>
</html>
```